TV Media buying firm needs Lead Gen page layout

We need a landing page using our current website look and feel to capture leads from our Chatterleaf ads. A quick form to capture Name, phone number, email, and a short message.
The call to action button should state "Get a free direct response campaign audit now!"
Updates

please visit www.brantlowmedia.com for the look and feel of the landing page.

I also uploaded a screenshot of what kind of landing page we are looking for.
the image has been reduced to 50% for the overall view.
thanks!

Please use our website's look and feel as reference for colors, fonts,header and footers.

The video placement on the sample file can be an image or combination image & text.

Again, please reference www.brantlowmedia.com for the look and feel.

Target Market(s)

50+ Market, Cheif Marketing Officer, Summit 1000 Companies

Industry/Entity Type

Tv

```html
<!DOCTYPE html>
<html lang="en">
<head>
<meta charset="utf-8">
<title>Brantlow Media – Free Campaign Audit</title>
<link rel="stylesheet" href="https://fonts.googleapis.com/css2?family=Arimo:ital,wght@0,400;0,700;1,700&family=Gochi+Hand&display=swap">
<style>
:root{
  --red:#d0121b;
  --red-dark:#a31d22;
  --ink:#1b1b1b;
  --text:#4a4a4a;
  --muted:#6b6b6b;
  --hero:#ececec;
  --panel:#ffffff;
  --form-bg:#e4e4e4;
  --footer:#4a4747;
  --gold:#f0b21f;
  --yellow:#ffd230;
  --green:#1fa81a;
  --topbar:#2f2f2f;
  --canvas:#dcdcdc;
}
*{box-sizing:border-box;margin:0;padding:0}
html,body{width:1200px;height:1000px;overflow:hidden}
body{background:var(--canvas);font-family:"Arimo",Arial,sans-serif;color:var(--text);position:relative}
.page{position:absolute;left:200px;top:10px;width:800px;height:990px;background:#e2e2e2;overflow:hidden}
.topbar{height:18px;background:var(--topbar);color:#e6e6e6;font-size:8px;line-height:18px;padding-left:75px}
.hero{position:absolute;top:18px;left:0;width:800px;height:397px;background:linear-gradient(135deg,#f4f4f4 0%,#e6e6e6 55%,#f0f0f0 100%);border-bottom:3px solid var(--red)}
.brand{position:absolute;left:61px;top:14px}
.brand-name{font-size:27px;font-weight:700;color:var(--ink);letter-spacing:-1px;line-height:27px}
.brand-tag{font-size:5px;color:var(--muted);margin-left:62px;letter-spacing:.3px}
.contact{position:absolute;right:74px;top:13px;text-align:right;font-weight:700;font-size:12px;color:var(--ink);line-height:16px}
.contact .phone{color:var(--red)}
.headline{position:absolute;left:61px;top:66px;font-size:20px;font-weight:700;color:var(--ink);line-height:25px}
.headline em{color:var(--red);font-size:24px}
.video{position:absolute;left:61px;top:144px;width:309px;height:191px;border:1px solid #999;background:#fff}
.video-still{height:171px;background:radial-gradient(ellipse at 40% 45%,#d7dbea 0%,#a5acd0 60%,#8a92bd 100%)}
.video-bar{height:19px;background:linear-gradient(#3a3a3a,#111);display:flex;align-items:center;gap:8px;padding:0 8px;color:#ddd;font-size:8px}
.video-bar .track{width:34px;height:3px;background:var(--red-dark)}
.video-bar .grow{flex:1}
.note{position:absolute;left:408px;top:124px;font-family:"Gochi Hand",cursive;font-size:12px;color:#333;line-height:14px;transform:rotate(-6deg)}
.arrow{position:absolute;left:412px;top:158px}
.lead-form{position:absolute;left:497px;top:66px;width:237px;height:306px;background:var(--panel);box-shadow:0 1px 3px rgba(0,0,0,.2)}
.lead-form h2{height:43px;background:var(--red);color:#fff;font-size:12px;text-align:center;line-height:15px;padding-top:7px;border:1px solid #b30f16}
.form-body{position:absolute;left:11px;top:54px;width:214px;height:240px;background:var(--form-bg)}
.field{display:flex;align-items:center;gap:6px;position:absolute;left:10px}
.field .ico{width:22px;height:22px;border-radius:50%;background:#bdbdbd;display:flex;align-items:center;justify-content:center}
.field .box{width:172px;height:22px;background:#fff;border:1px solid #ccc;font-size:9px;color:#999;line-height:20px;padding-left:8px}
.field .box b{color:var(--red);font-weight:400}
.cta{position:absolute;left:9px;top:184px;width:197px;height:38px;border-radius:19px;background:linear-gradient(#ffe15c,var(--gold));border:1px solid #e0a000;font-size:10px;font-weight:700;color:#3a2a00;text-align:center;line-height:36px}
.privacy{position:absolute;left:0;top:228px;width:214px;text-align:center;font-size:7px;color:#555}
.logo-strip{position:absolute;top:418px;left:0;width:800px;height:58px;background:linear-gradient(#ffffff,#e4e4e4);display:flex;align-items:center;justify-content:center;gap:26px}
.logo-strip span,.client-row span{font-size:20px;font-weight:700;letter-spacing:-.5px}
.logo-strip span{color:#333}
.content-card{position:absolute;left:24px;top:490px;width:753px;height:305px;background:#fff;border:1px solid #ccc;border-radius:3px 3px 0 0}
.feature{position:absolute;width:220px}
.feature .hex{position:absolute;left:0;top:0}
.feature h3{position:absolute;left:42px;top:0;width:178px;font-size:12px;font-weight:400;color:var(--ink);padding-bottom:6px;border-bottom:1px dashed #999}
.feature ul{position:absolute;left:48px;top:26px;width:175px;list-style:none}
.feature li{font-size:9px;line-height:12px;margin-bottom:7px;position:relative;padding-left:10px}
.feature li::before{content:"";position:absolute;left:0;top:4px;width:3px;height:3px;background:var(--red)}
.testimonial{position:absolute;left:508px;top:19px;width:220px}
.avatar{position:absolute;left:0;top:0;width:37px;height:37px;border-radius:50%;background:linear-gradient(#f5d9cc,#d9a797);border:3px solid #eee}
.testimonial h4{position:absolute;left:47px;top:6px;width:168px;font-size:12px;font-style:italic;color:var(--ink);padding-bottom:4px;border-bottom:1px dashed #999}
.quote{position:absolute;left:49px;top:30px;width:172px;font-size:9px;line-height:12px}
.quote p{margin-bottom:5px}
.quote .who{font-weight:700;color:#444}
.learn{position:absolute;left:534px;top:182px;width:205px;text-align:center;font-size:9px;font-weight:700;color:var(--ink);padding-bottom:6px;border-bottom:1px solid #ddd}
.visit{position:absolute;left:592px;top:213px;width:100px;height:32px;background:linear-gradient(#2fc22a,var(--green));border:1px solid #138a10;color:#fff;font-size:10px;font-weight:700;text-align:center;line-height:30px}
.site-footer{position:absolute;left:24px;top:795px;width:753px;height:180px;background:var(--footer);color:#fff}
.site-footer h5{position:absolute;left:28px;top:12px;width:640px;font-size:11px;font-weight:400;padding-bottom:8px;border-bottom:1px solid #5c5959}
.client-row{position:absolute;left:32px;top:48px;display:flex;gap:14px;align-items:center}
.client-row span{color:#fff}
.office{position:absolute;top:104px;font-size:7px;line-height:12px;color:#eee}
.office h6{font-size:11px;color:var(--gold);font-weight:400;margin-bottom:3px}
.footer-links{position:absolute;left:462px;top:106px;font-size:8px;font-weight:700;line-height:15px}
</style>
</head>
<body>
<main class="page">
  <div class="topbar">DRTV, Media Buying, Direct Response Television, DRTV Advertising, World Class Media Buying Agency - Brantlow Media</div>

  <section class="hero">
    <div class="brand">
      <div class="brand-name">brantlowmedia</div>
      <div class="brand-tag">MULTI-CHANNEL DIRECT RESPONSE</div>
    </div>
    <div class="contact">Contact Us:<br><span class="phone">(555) 732 6110</span></div>

    <h1 class="headline">Are Your Marketing Campaings<br>Been <em>Efficient?</em></h1>

    <div class="video">
      <div class="video-still" role="img" aria-label="Video still: title card asking what direct response television is"></div>
      <div class="video-bar">
        <svg width="8" height="9" viewBox="0 0 8 9"><path d="M0 0L8 4.5L0 9Z" fill="#ddd"/></svg>
        <svg width="10" height="9" viewBox="0 0 10 9"><path d="M0 3h3l3-3v9l-3-3H0Z" fill="#ddd"/></svg>
        <span class="track"></span>
        <span>0:00 / 3:34</span>
        <span class="grow"></span>
        <svg width="9" height="9" viewBox="0 0 9 9"><path d="M0 3V0h3M6 0h3v3M9 6v3H6M3 9H0V6" stroke="#ddd" fill="none"/></svg>
      </div>
    </div>

    <div class="note">Get Your FREE<br>Report, Now!</div>
    <svg class="arrow" width="70" height="30" viewBox="0 0 70 30"><path d="M2 20Q30 34 66 10" stroke="#222" stroke-width="1.5" fill="none"/><path d="M58 8L67 9L62 17" stroke="#222" stroke-width="1.5" fill="none"/></svg>

    <form class="lead-form">
      <h2>DISCOVER If You’r Wasting Money<br>On Your Marketing Camapaings!</h2>
      <div class="form-body">
        <div class="field" style="top:7px"><span class="ico"><svg width="10" height="10" viewBox="0 0 10 10"><circle cx="5" cy="3" r="2.3" fill="none" stroke="#fff"/><path d="M1 10Q5 4 9 10" fill="none" stroke="#fff"/></svg></span><span class="box">Name <b>*</b></span></div>
        <div class="field" style="top:42px"><span class="ico"><svg width="10" height="8" viewBox="0 0 10 8"><rect x=".5" y=".5" width="9" height="7" fill="none" stroke="#fff"/><path d="M.5 .5L5 4.5L9.5 .5" fill="none" stroke="#fff"/></svg></span><span class="box">Email <b>*</b></span></div>
        <div class="field" style="top:77px"><span class="ico"><svg width="7" height="11" viewBox="0 0 7 11"><rect x=".5" y=".5" width="6" height="10" rx="1" fill="none" stroke="#fff"/></svg></span><span class="box">Phone <b>*</b></span></div>
        <div class="field" style="top:111px"><span class="ico"><svg width="10" height="10" viewBox="0 0 10 10"><path d="M3 7L7 3M2 5L1 6a2 2 0 0 0 3 3l1-1M8 5l1-1a2 2 0 0 0-3-3L5 2" fill="none" stroke="#fff"/></svg></span><span class="box">Web site Url <b>*</b></span></div>
        <div class="field" style="top:142px"><span class="ico"><svg width="10" height="10" viewBox="0 0 10 10"><rect x=".5" y="1.5" width="8" height="8" fill="none" stroke="#fff"/><path d="M4 6L9 1" stroke="#fff"/></svg></span><span class="box">Message <b>*</b></span></div>
        <div class="cta">Get A Free Online Marketing Audit!</div>
        <p class="privacy">We will NOT share your email or Spam you!</p>
      </div>
    </form>
  </section>

  <div class="logo-strip">
    <span>Skyline TV</span><span>HealthPage</span><span>Ironworks</span><span>TaxPilot</span><span>Bigwall</span>
  </div>

  <section class="content-card">
    <div class="feature" style="left:15px;top:21px">
      <svg class="hex" width="32" height="30" viewBox="0 0 32 30"><path d="M8 0h16l8 15-8 15H8L0 15Z" fill="var(--red-dark)"/><path d="M10 12h3l6-4v14l-6-4h-3Z" fill="none" stroke="#fff"/></svg>
      <h3>Dummy Title Text Example</h3>
      <ul><li>Improve your comapny's online brand exposure.</li><li>Build your website organic search engine ranking</li><li>Improve your comapny's online brand exposure.</li></ul>
    </div>
    <div class="feature" style="left:266px;top:23px">
      <svg class="hex" width="32" height="30" viewBox="0 0 32 30"><path d="M8 0h16l8 15-8 15H8L0 15Z" fill="var(--red-dark)"/><rect x="10" y="9" width="12" height="12" fill="none" stroke="#fff"/><path d="M11 18l4-4 3 2 3-4" fill="none" stroke="#fff"/></svg>
      <h3>Dummy Title Text Example</h3>
      <ul><li>Improve your comapny's online brand exposure.</li><li>Build your website organic search engine ranking</li><li>Improve your comapny's online brand exposure.</li></ul>
    </div>
    <div class="feature" style="left:15px;top:157px">
      <svg class="hex" width="32" height="30" viewBox="0 0 32 30"><path d="M8 0h16l8 15-8 15H8L0 15Z" fill="var(--red-dark)"/><ellipse cx="16" cy="15" rx="7" ry="3" fill="none" stroke="#fff"/><ellipse cx="16" cy="15" rx="3" ry="7" fill="none" stroke="#fff"/><circle cx="16" cy="15" r="1.3" fill="#fff"/></svg>
      <h3>Dummy Title Text Example</h3>
      <ul><li>Improve your comapny's online brand exposure.</li><li>Build your website organic search engine ranking</li><li>Improve your comapny's online brand exposure.</li></ul>
    </div>
    <div class="feature" style="left:266px;top:159px">
      <svg class="hex" width="32" height="30" viewBox="0 0 32 30"><path d="M8 0h16l8 15-8 15H8L0 15Z" fill="var(--red-dark)"/><rect x="9" y="10" width="14" height="9" fill="none" stroke="#fff"/><path d="M16 19v3M12 22h8" stroke="#fff"/></svg>
      <h3>Dummy Title Text Example</h3>
      <ul><li>Improve your comapny's online brand exposure.</li><li>Build your website organic search engine ranking</li><li>Improve your comapny's online brand exposure.</li></ul>
    </div>

    <div class="testimonial">
      <div class="avatar" role="img" aria-label="Portrait of the quoted client"></div>
      <h4>Testimonial</h4>
      <div class="quote">
        <p>“Lorem ipsum dolor sit amet, consectetu adipisicing elit, sed do eiusmod tempor incididunt ut labore et dolore magna ali.</p>
        <p>Ut enim ad minim veniam, quis nostrud exercitation ullamco laboris nisi ut aliq uip ex ea commodo consequat”</p>
        <p class="who">CEO Daniel R.</p>
      </div>
    </div>
    <p class="learn">Do You Want To Learn More...?</p>
    <div class="visit">Visit Our Site!</div>
  </section>

  <footer class="site-footer">
    <h5>Our Clients</h5>
    <div class="client-row">
      <span>Skyline TV</span><span>HealthPage</span><span>Ironworks</span><span>Bigwall</span><span>HealthPage</span><span>Ironworks</span>
    </div>
    <div class="office" style="left:26px"><h6>Head Quarters</h6>1110, Street Suite 101<br>Bayview, California 98651<br>Call: (555) 234 972<br>Mobile: (555) 6358 937</div>
    <div class="office" style="left:171px"><h6>Las Vegas</h6>1110, Street Suite 101<br>Bayview, California 98651<br>Call: (555) 234 972<br>Mobile: (555) 6358 937</div>
    <div class="office" style="left:319px"><h6>Nueva York</h6>1110, Street Suite 101<br>Bayview, California 98651<br>Call: (555) 234 972<br>Mobile: (555) 6358 937</div>
    <nav class="footer-links">Contact Us<br>Site Map<br>Privacy Police</nav>
  </footer>
</main>
</body>
</html>
```